Thank You Card for Customer Purchase

I need a thank you card designed to go out with my product once a customer has purchased. It will require some content creation but only a couple of lines.

It needs be basically state something along the lines of

"Thank you for your purchase..........
as well as some sort of speal about the company as well as contact details"

I have attached our brand guide to assist you. I will also provide you the url so you may get an idea of the company and the way we talk.

The document should be double sided A5 In size Landscape and be print ready as well. Provided in illustrator and pdf files. I have attached a template that is to be used and there is a printing instructions PDF document you need to follow as well.

Please contact if you have any questions

Target Market(s)

Young people aroung 20-40 male and female. Cool people

Industry/Entity Type

Printing

Requirements
Must have
• be cool and inline with brand guideline. please check out www.mabelfrost.com.au for ideas.

```html
<!DOCTYPE html>
<html lang="en">
<head>
<meta charset="utf-8">
<title>Mabel Frost – Thank You Card</title>
<link rel="stylesheet" href="https://fonts.googleapis.com/css2?family=Josefin+Sans:wght@300&family=Roboto+Condensed:ital,wght@0,400;1,700&family=Courier+Prime:wght@400;700&display=swap">
<style>
  :root {
    --page: #ffffff;
    --card: #dcdedb;
    --ink: #55565a;
    --ink-soft: #3f4044;
  }
  * { margin: 0; padding: 0; box-sizing: border-box; }
  html, body {
    width: 816px;
    height: 1200px;
    overflow: hidden;
    background: var(--page);
  }
  .sheet {
    position: relative;
    width: 816px;
    height: 1200px;
  }
  .card {
    position: absolute;
    left: 22px;
    width: 772px;
    height: 536px;
    background: var(--card);
    color: var(--ink);
    text-align: center;
  }
  .card--front { top: 22px; }
  .card--back { top: 640px; }

  .brand-name {
    position: absolute;
    left: 0; right: 0;
    top: 232px;
    font-family: "Josefin Sans", sans-serif;
    font-weight: 300;
    font-size: 50px;
    letter-spacing: 0.32em;
    padding-left: 0.32em;
    color: var(--ink);
  }
  .contact-line {
    position: absolute;
    left: 0; right: 0;
    top: 474px;
    font-family: "Courier Prime", monospace;
    font-size: 14px;
    color: var(--ink-soft);
  }

  .thanks {
    position: absolute;
    left: 0; right: 0;
    top: 96px;
    font-family: "Roboto Condensed", sans-serif;
    font-style: italic;
    font-weight: 700;
    color: var(--ink);
    line-height: 1;
  }
  .thanks__main {
    display: block;
    font-size: 128px;
    letter-spacing: 0.01em;
  }
  .thanks__sub {
    display: block;
    margin-top: 16px;
    font-size: 62px;
    letter-spacing: 0.06em;
  }
  .tagline {
    position: absolute;
    left: 0; right: 0;
    top: 348px;
    font-family: "Roboto Condensed", sans-serif;
    font-size: 19px;
    letter-spacing: 0.18em;
    color: var(--ink);
  }
  .disclaimer {
    position: absolute;
    left: 186px;
    width: 400px;
    top: 470px;
    font-family: "Courier Prime", monospace;
    font-size: 9px;
    line-height: 1.3;
    text-align: left;
    color: var(--ink-soft);
  }
  .disclaimer strong { font-weight: 700; }
</style>
</head>
<body>
  <main class="sheet">
    <section class="card card--front" aria-label="Card front">
      <h1 class="brand-name">MABEL FROST</h1>
      <p class="contact-line">www.mabelfrost.com.au | T: 1300 555 204</p>
    </section>

    <section class="card card--back" aria-label="Card back">
      <h2 class="thanks">
        <span class="thanks__main">THANK YOU</span>
        <span class="thanks__sub">FOR YOUR PURCHASE</span>
      </h2>
      <p class="tagline">ENJOY YOUR SWEET NEW SPECS!</p>
      <p class="disclaimer"><strong>Disclaimer:</strong> Mabel is highly addictive. We cannot be held responsible for any endless shopping habits that may be formed as a result of buying our products.</p>
    </section>
  </main>
</body>
</html>
```